brix4lane

i want to ues this logo and the same colors used on the business card

cleaning & service

Industry/Entity Type

Business

Contact Information for Business Card

Font styles to use
Serif
Sans Serif
Decorative
Script

Colors
add136
0692cd
000000
5c5c5c
fbfbfb

Requirements
Must have
• cleaning things

```html
<!DOCTYPE html>
<html lang="en">
<head>
<meta charset="UTF-8">
<title>brix4lane – Business Card</title>
<link href="https://fonts.googleapis.com/css2?family=Open+Sans:wght@400;600;700&display=swap" rel="stylesheet">
<style>
  :root {
    --blue: #0e6fb8;
    --green: #add136;
    --ink: #1f1f1f;
    --ink-soft: #3a3a3a;
    --card-back: #e9eded;
    --card-front: #ffffff;
    --stage: #d9d9d9;
  }
  * { margin: 0; padding: 0; box-sizing: border-box; }
  html, body {
    width: 1200px;
    height: 844px;
    overflow: hidden;
  }
  body {
    background: var(--stage);
    font-family: "Open Sans", sans-serif;
    position: relative;
  }
  .card {
    position: absolute;
    top: 279px;
    width: 500px;
    height: 286px;
    overflow: hidden;
    box-shadow: 0 6px 18px rgba(0,0,0,0.18);
  }

  /* Contact side */
  .card--contact {
    left: 70px;
    background: var(--card-back);
    border-top: 14px solid var(--blue);
    border-bottom: 14px solid var(--blue);
  }
  .contact {
    position: absolute;
    left: 0; right: 0;
    top: 70px;
    text-align: center;
    color: var(--ink);
  }
  .contact__name {
    display: inline-block;
    font-size: 17px;
    font-weight: 700;
    letter-spacing: 0.3px;
    padding: 0 4px 3px;
    border-bottom: 1px solid var(--blue);
  }
  .contact__role {
    font-size: 13px;
    color: var(--ink-soft);
    margin-top: 3px;
  }
  .contact__phone {
    font-size: 14px;
    margin-top: 24px;
    color: var(--ink-soft);
  }
  .contact__email {
    font-size: 14.5px;
    margin-top: 3px;
  }

  /* Brand side */
  .card--brand {
    left: 630px;
    background: var(--card-front);
  }
  .tab {
    position: absolute;
    width: 26px;
    height: 40px;
    background: var(--blue);
  }
  .tab--left {
    left: 0;
    top: 164px;
    border-right: 5px solid var(--green);
  }
  .tab--right {
    right: 0;
    top: 44px;
    border-left: 5px solid var(--green);
  }
  .brand {
    position: absolute;
    left: 0; right: 0;
    top: 0; bottom: 0;
    display: flex;
    align-items: center;
    justify-content: center;
    gap: 10px;
  }
  .brand__dot {
    width: 20px;
    height: 20px;
    border-radius: 50%;
    background: var(--green);
  }
  .brand__name {
    font-size: 30px;
    font-weight: 700;
    color: var(--blue);
  }
</style>
</head>
<body>
  <section class="card card--contact">
    <div class="contact">
      <p class="contact__name">DANIEL MARSH</p>
      <p class="contact__role">Managing Director</p>
      <p class="contact__phone">044-312-5568</p>
      <p class="contact__email">hello@brix4lane.com</p>
    </div>
  </section>

  <section class="card card--brand">
    <span class="tab tab--left"></span>
    <span class="tab tab--right"></span>
    <div class="brand">
      <span class="brand__dot"></span>
      <span class="brand__name">brix4lane</span>
    </div>
  </section>
</body>
</html>
```